Consulting im Pharmaproduktionsbereich sucht Webdesign
Zielgruppe
Consulting im Pharmaproduktionsbereich.
Bitte lesen Sie dazu die PowerPoint.
Aufgabenstellung
Im Anhang finden Sie eine Powerpoint Datei, von welcher die 'Home' und 'Referenz'seite Teil dieser Auschreibung sind.

```html
<!DOCTYPE html>
<html lang="de">
<head>
<meta charset="utf-8">
<title>Referenzen – Nordlicht Tec GmbH</title>
<link href="https://fonts.googleapis.com/css2?family=Open+Sans:ital,wght@0,400;0,600;1,400&family=Raleway:wght@400;600&family=Tinos:wght@700&display=swap" rel="stylesheet">
<style>
  :root {
    --brand: #17488a;
    --ink: #111;
    --muted: #555;
    --rule: #cfcfcf;
    --white: #fff;
    --photo-a: #8fa6bd;
    --photo-b: #3e5670;
  }
  * { box-sizing: border-box; margin: 0; padding: 0; }
  html, body { width: 1200px; height: 816px; overflow: hidden; background: var(--white); }
  body { position: relative; font-family: "Open Sans", sans-serif; color: var(--ink); }

  .site-header {
    position: absolute; left: 0; top: 0; width: 1200px; height: 84px;
    background: var(--white); box-shadow: 0 2px 5px rgba(0,0,0,.15);
  }
  .brand {
    position: absolute; left: 56px; top: 26px;
    display: flex; align-items: center; gap: 10px;
    font-family: "Raleway", sans-serif; font-weight: 600; font-size: 28px; color: var(--brand);
    letter-spacing: -0.5px;
  }
  .brand-mark { width: 22px; height: 22px; background: var(--brand); }
  .main-nav {
    position: absolute; right: 61px; top: 24px; height: 27px;
    display: flex; align-items: center;
    font-family: "Raleway", sans-serif; font-size: 14.5px; color: var(--ink);
  }
  .main-nav a { color: inherit; text-decoration: none; padding: 0 7px; line-height: 27px; }
  .main-nav a.home { font-weight: 600; padding-left: 0; }
  .main-nav a.active { background: var(--brand); color: var(--white); }
  .main-nav .sep { padding: 0 12px; }

  .intro { position: absolute; left: 54px; top: 168px; }
  .intro h1 { font-family: "Tinos", serif; font-weight: 700; font-size: 39px; color: var(--brand); line-height: 1; }
  .intro p { font-style: italic; font-size: 21px; color: var(--muted); margin-top: 6px; }

  .accordion { position: absolute; left: 54px; top: 295px; width: 486px; border-top: 1px solid var(--rule); }
  .acc-item { border-bottom: 1px solid var(--rule); }
  .acc-head {
    display: flex; justify-content: space-between; align-items: center;
    height: 51px; padding: 0 10px 0 2px; font-size: 19px; color: var(--brand);
  }
  .acc-item.open .acc-head { height: 45px; padding-left: 0; border-bottom: 1px solid var(--rule); }
  .acc-icon { width: 14px; height: 14px; }
  .acc-body { padding: 14px 6px 11px 2px; font-size: 10.8px; line-height: 13.5px; }

  .hero-photo {
    position: absolute; left: 607px; top: 183px; width: 538px; height: 359px;
    background: linear-gradient(100deg, var(--photo-b), var(--photo-a) 45%, #c9d3dc 70%, var(--photo-b));
  }

  .site-footer {
    position: absolute; left: 0; top: 766px; width: 1200px; height: 50px;
    background: var(--brand); color: var(--white);
    font-family: "Raleway", sans-serif; font-size: 14.5px;
    display: flex; align-items: center; justify-content: space-between; padding: 0 57px 0 55px;
  }
  .footer-nav a { color: inherit; text-decoration: none; }
  .footer-nav a.home { font-weight: 600; }
  .footer-nav .sep { padding: 0 12px; }
  .footer-nav .sep.tight { padding: 0 6px; }
</style>
</head>
<body>
  <header class="site-header">
    <div class="brand"><span class="brand-mark"></span>Nordlicht Tec GmbH</div>
    <nav class="main-nav">
      <a class="home" href="#">HOME</a><span>|</span>
      <a class="active" href="#" style="margin-left:8px">REFERENZEN</a><span class="sep">|</span>
      <a href="#" style="padding:0">KONTAKT</a><span class="sep">|</span>
      <a href="#" style="padding:0">IMPRESSUM</a>
    </nav>
  </header>

  <section class="intro">
    <h1>Referenzen</h1>
    <p>Lorem ipsum lorem itum names</p>
  </section>

  <section class="accordion">
    <div class="acc-item open">
      <div class="acc-head">Time Tracking
        <svg class="acc-icon" viewBox="0 0 14 14"><line x1="0" y1="7" x2="14" y2="7" stroke="#888" stroke-width="1"/></svg>
      </div>
      <div class="acc-body">Internationale Aufsichtbehörden fordern eine immer genauere Dokumentation &amp; Rückverfolgbarkeit Ihrer Produktionsschritte. Speziell die von Personen durchgeführte optische Produktkontrolle stellt dabei ein großes Risiko während einer Inspektion dar. Unser FDA-zertifiziertes System sorgt mit einfachen und sicheren Funktionen für eine behördlich anerkannte Protokollierung. Eine Mehrstufige Authentifizierung und einer detailierte Qualifizierungsmatrix inklusive.</div>
    </div>
    <div class="acc-item"><div class="acc-head">Geographische Lokalisierung
      <svg class="acc-icon" viewBox="0 0 14 14"><path d="M0 7H14M7 0V14" stroke="#888" stroke-width="1"/></svg></div></div>
    <div class="acc-item"><div class="acc-head">Org Chart
      <svg class="acc-icon" viewBox="0 0 14 14"><path d="M0 7H14M7 0V14" stroke="#888" stroke-width="1"/></svg></div></div>
    <div class="acc-item"><div class="acc-head">OEE
      <svg class="acc-icon" viewBox="0 0 14 14"><path d="M0 7H14M7 0V14" stroke="#888" stroke-width="1"/></svg></div></div>
    <div class="acc-item"><div class="acc-head">Modellierung Geschäftsprozesse
      <svg class="acc-icon" viewBox="0 0 14 14"><path d="M0 7H14M7 0V14" stroke="#888" stroke-width="1"/></svg></div></div>
    <div class="acc-item"><div class="acc-head">Multiparameter Optimierung
      <svg class="acc-icon" viewBox="0 0 14 14"><path d="M0 7H14M7 0V14" stroke="#888" stroke-width="1"/></svg></div></div>
  </section>

  <div class="hero-photo" role="img" aria-label="Foto: Mitarbeiter in Schutzkleidung prüft mit Klemmbrett Anlagen in einer Pharmaproduktion"></div>

  <footer class="site-footer">
    <nav class="footer-nav">
      <a class="home" href="#">HOME</a><span class="sep tight">|</span>
      <a href="#">REFERENZEN</a><span class="sep">|</span>
      <a href="#">KONTAKT</a><span class="sep">|</span>
      <a href="#">IMPRESSUM</a><span class="sep">|</span>
      <a href="#">DATENSCHUTZ</a>
    </nav>
    <span class="copyright">© Nordlicht Tec GmbH 2019. All rights reserved.</span>
  </footer>
</body>
</html>
```